North American Image Consultant needs a process design and a method design

I am an Image/style consultant who works with business professionals in the Toronto area. My product name is called " R.E.S.K.A." I help people understand how your " Position, Industry, Volume, effects their Outcome and Time. I help people create a professional appearance in a business casual/digital world, from head to toe. I work with them through all 4 seasons, to achieve consistency and confidence to help them look and feel amazing, inside and out.. easily and effortlessly. My main colour is aqua blue, I don't want any neon or primary colours. I would like it to appeal to both men and women ( but mostly women)
The final design should be an easy to follow path to success with an understanding of what R.E.S.K.A will do for them.

Target Market(s)

mid level executive business professionals 38-58 yrs old they want to look and feel amazing inside and out. They want to up their game, get the promotion, nail the interview , and feel they're relevant and taken seriously in a leadership way.

Font styles to use
Serif

Colors
b7a5cd
886aae
85cae6
33a6d7
33b8a4
f04a50
00a990
e34297
85acd3

Requirements
Must have
• A classy, casual feel. A positive feel good feeling
Nice to have
• A 3 colour balance ( Not black based)
Should not have
• Too many squares
too many squiggly lines.
Not too masculine/feminine
too childish/youthful
Not office focused or bank focused

```html
<!DOCTYPE html>
<html lang="en">
<head>
<meta charset="utf-8">
<title>Maintaining a Professional Appearance</title>
<link rel="stylesheet" href="https://fonts.googleapis.com/css2?family=Lato:wght@300;400;700;900&family=Tinos&display=swap">
<style>
  :root {
    --band-blue: #94c6e2;
    --ink: #2b2b2e;
    --letter-red: #e2474c;
    --path-purple: #5e3d9a;
    --path-lilac: #b7a5cd;
    --path-sky: #85cae6;
    --path-aqua: #33a6d7;
    --page-white: #ffffff;
    --page-mist: #e4eff7;
  }
  * { margin: 0; padding: 0; box-sizing: border-box; }
  html, body { width: 1200px; height: 927px; overflow: hidden; background: var(--page-white); }
  .poster {
    position: relative;
    width: 1200px;
    height: 927px;
    overflow: hidden;
    background: linear-gradient(160deg, var(--page-white) 45%, var(--page-mist) 100%);
    font-family: "Lato", sans-serif;
    color: var(--ink);
  }
  .side-band {
    position: absolute;
    inset: 0;
    background: var(--band-blue);
    clip-path: polygon(0 0, 548px 0, 44px 927px, 0 927px);
  }
  .title {
    position: absolute;
    left: 94px;
    top: 56px;
    font-weight: 900;
    font-size: 56.5px;
    letter-spacing: -0.4px;
    line-height: 1;
    white-space: nowrap;
  }
  .subtitle {
    position: absolute;
    left: 96px;
    top: 124px;
    font-weight: 400;
    font-size: 36px;
    line-height: 1;
    white-space: nowrap;
  }
  .pivot-path {
    position: absolute;
    left: 0;
    top: 0;
    width: 1200px;
    height: 927px;
  }
  .step {
    position: absolute;
    top: 222px;
    width: 158px;
    margin-left: -79px;
    text-align: center;
  }
  .step-letter {
    display: block;
    font-weight: 300;
    font-size: 62px;
    line-height: 1;
    color: var(--letter-red);
    height: 68px;
  }
  .step-name {
    display: block;
    font-weight: 900;
    font-size: 21px;
    line-height: 1;
    margin-top: 9px;
  }
  .step-text {
    display: block;
    font-size: 17.5px;
    line-height: 22px;
    margin-top: 13px;
  }
  .intro {
    position: absolute;
    left: 94px;
    top: 526px;
    width: 275px;
    font-family: "Tinos", serif;
    font-size: 14.2px;
    line-height: 18.3px;
  }
  .intro p + p { margin-top: 17px; }
  .intro .line {
    display: block;
    white-space: nowrap;
    text-align: justify;
    text-align-last: justify;
  }
  .intro .line.end { text-align: left; text-align-last: left; }
  .team-scene {
    position: absolute;
    left: 392px;
    top: 520px;
    width: 760px;
    height: 378px;
    border-radius: 14px 14px 50% 50% / 14px 14px 30px 30px;
    background: linear-gradient(180deg, #f3dbe6 0%, #c98ab3 45%, #8a4f86 72%, #1e8ea6 100%);
    opacity: 0.85;
  }
</style>
</head>
<body>
<main class="poster">
  <div class="side-band"></div>

  <h1 class="title">Maintaining a Professional Appearance</h1>
  <h2 class="subtitle">In a Business Casual World</h2>

  <svg class="pivot-path" viewBox="0 0 1500 1159" aria-hidden="true">
    <defs>
      <linearGradient id="pathGradient" gradientUnits="userSpaceOnUse" x1="120" y1="0" x2="1381" y2="0">
        <stop offset="0" stop-color="var(--path-purple)"/>
        <stop offset="0.38" stop-color="var(--path-lilac)"/>
        <stop offset="0.7" stop-color="var(--path-sky)"/>
        <stop offset="1" stop-color="var(--path-aqua)"/>
      </linearGradient>
    </defs>
    <g fill="none" stroke="url(#pathGradient)" stroke-width="5" stroke-linejoin="round">
      <path d="M318,347 V300 Q318,270 288,270 H150 Q120,270 120,300 V535 Q120,565 150,565 H288 Q318,565 318,535 V470 L385,360 V300 Q385,270 415,270 H553 Q583,270 583,300 V347"/>
      <path d="M385,490 V535 Q385,565 415,565 H553 Q583,565 583,535 V470 L651,360 V300 Q651,270 681,270 H819 Q849,270 849,300 V347"/>
      <path d="M651,490 V535 Q651,565 681,565 H819 Q849,565 849,535 V470 L917,360 V300 Q917,270 947,270 H1085 Q1115,270 1115,300 V347"/>
      <path d="M917,490 V535 Q917,565 947,565 H1085 Q1115,565 1115,535 V470 L1183,360 V300 Q1183,270 1213,270 H1351 Q1381,270 1381,300 V535 Q1381,565 1351,565 H1213 Q1183,565 1183,535 V490"/>
    </g>
    <g>
      <circle cx="318" cy="347" r="11" fill="#8a6db0"/>
      <circle cx="385" cy="490" r="11" fill="#9a80bd"/>
      <circle cx="583" cy="347" r="11" fill="#ad9bcb"/>
      <circle cx="651" cy="490" r="11" fill="#b5b2d8"/>
      <circle cx="849" cy="347" r="11" fill="#9ec8e4"/>
      <circle cx="917" cy="490" r="11" fill="#8fcbe6"/>
      <circle cx="1115" cy="347" r="11" fill="#6bbbe2"/>
      <circle cx="1183" cy="490" r="11" fill="#4cafdc"/>
    </g>
  </svg>

  <div class="step" style="left:175px">
    <span class="step-letter">P</span>
    <span class="step-name">POSITION</span>
    <span class="step-text">Level of<br>authority</span>
  </div>
  <div class="step" style="left:387px">
    <span class="step-letter">I</span>
    <span class="step-name">INDUSTRY</span>
    <span class="step-text">Influence of<br>environment</span>
  </div>
  <div class="step" style="left:600px">
    <span class="step-letter">V</span>
    <span class="step-name">VOLUME</span>
    <span class="step-text">The ‘Sound,’ of<br>your presence<br>when you walk<br>into a room</span>
  </div>
  <div class="step" style="left:813px">
    <span class="step-letter">O</span>
    <span class="step-name">OUTCOME</span>
    <span class="step-text">Achieve consis<br>tent results</span>
  </div>
  <div class="step" style="left:1026px">
    <span class="step-letter">T</span>
    <span class="step-name">TIME</span>
    <span class="step-text">Save more,<br>spend less</span>
  </div>

  <section class="intro">
    <p>
      <span class="line">Lorem ipsum dolor sit amet, consectetuer</span>
      <span class="line">adipiscing elit, sed diam nonummy nibh</span>
      <span class="line">euismod tincidunt ut laoreet dolore magna</span>
      <span class="line">aliquam erat volutpat. Ut wisi enim ad minim</span>
      <span class="line">veniam, quis nostrud exerci tation ullamcorper</span>
      <span class="line end">suscipit lobortis.</span>
    </p>
    <p>
      <span class="line">Lorem ipsum dolor sit amet, consectetuer</span>
      <span class="line">adipiscing elit, sed diam nonummy nibh</span>
      <span class="line">euismod tincidunt ut laoreet dolore magna</span>
      <span class="line end">aliquam erat volutpat.</span>
    </p>
    <p>
      <span class="line">Ut wisi enim ad minim veniam, quis nostrud</span>
      <span class="line">exerci tation ullamcorper suscipit lobortis nisl</span>
      <span class="line end">ut aliquip ex ea commodo consequat.</span>
    </p>
  </section>

  <div class="team-scene" role="img" aria-label="Illustration of four businesswomen chatting with coffee cups beside a desk with computer monitors, a potted plant and an office chair"></div>
</main>
</body>
</html>
```